In Home Senior Care Agency Business Card Design Needed

At Silver Birch Helpers, we don't just work in the care-giving industry. We truly care.

We are dedicated to providing personable, hands-on and integrated caring services that aim to help people maintain safe and comfortable life standards within the familiar settings of their own homes.

We would like to see designs that use my logo colors obviously. The final design will be modern, yet professional and semi-minimalistic. It should communicate an well-established company that is innovative. We would also like the design to have that 'flat' design look. Ideally having the design roll over to the backend of the card. Most likely it will be printed on a Matte paper with a die cut (either 2 rounded corners -leaf cut) or all rounded.

Target Market(s)

Baby boomer generation. 45 years and older.

Industry/Entity Type

Business

Contact Information for Business Card

Text for Front:
Slogan somewhere "Our Family. Caring For Yours.”

Darren Whitlow
President

Cell: 917.284.6051
Phone: 917.512.7368
E: Darren@silverbirchhelpers.com
W: www.SilverBirchHelpers.com

Back:
-Meal Preparation
-Transportation
-Light Housekeeping
-Bathing Assistance
-Companionship

Font styles to use
Serif
Sans Serif

Requirements
Must have
• Flat, modern, professional design. Not too many colors. Match my colors in logo. Design of card must reflect from the front onto the back. Evenly spaced font.
Nice to have
• Try to work off current logo scheme, but logo may need to be redesigned.
Should not have
• Not too many colors.

```html
<!DOCTYPE html>
<html lang="en">
<head>
<meta charset="utf-8">
<title>Silver Birch Helpers – Business Card</title>
<link href="https://fonts.googleapis.com/css2?family=Open+Sans:wght@400;600;700&display=swap" rel="stylesheet">
<style>
  :root {
    --olive: #857449;
    --green: #10773c;
    --gold: #f6b94f;
    --ink: #3a3a3a;
    --card-light: #ffffff;
    --card-shade: #e4e4e4;
    --backdrop: #efece7;
  }
  * { margin: 0; padding: 0; box-sizing: border-box; }
  html, body {
    width: 1200px; height: 900px; overflow: hidden;
    background: var(--backdrop);
    font-family: "Open Sans", sans-serif;
  }
  .stage { position: relative; width: 1200px; height: 900px; }

  .card {
    position: absolute; top: 301px;
    width: 520px; height: 298px;
    background: radial-gradient(ellipse at 60% 35%, var(--card-light) 0%, #f6f6f6 45%, var(--card-shade) 100%);
    box-shadow: 0 6px 18px rgba(0,0,0,0.18);
    overflow: hidden;
  }
  .card--front { left: 50px; }
  .card--back  { left: 630px; }

  .card-bands { position: absolute; left: 0; top: 0; width: 520px; height: 298px; }

  /* Front */
  .contact { position: absolute; left: 30px; top: 26px; }
  .contact__name { font-weight: 700; font-size: 19px; color: var(--green); letter-spacing: 0.3px; }
  .contact__title { font-size: 12px; color: var(--ink); margin-top: 2px; margin-bottom: 14px; }
  .contact__list { list-style: none; }
  .contact__item {
    display: flex; align-items: center; gap: 8px;
    font-size: 10.5px; color: var(--ink); line-height: 19px;
  }
  .contact__icon { width: 10px; height: 10px; flex: none; }

  .brand { position: absolute; left: 290px; top: 108px; width: 210px; }
  .brand__row { display: flex; align-items: center; gap: 8px; }
  .brand__dot { width: 14px; height: 14px; border-radius: 50%; background: var(--olive); flex: none; }
  .brand__name { font-weight: 700; font-size: 22px; line-height: 25px; color: var(--green); }
  .brand__slogan {
    margin-top: 8px; padding-left: 22px;
    font-size: 10.5px; font-weight: 600; color: var(--olive); letter-spacing: 0.2px;
  }

  .front-web {
    position: absolute; right: 46px; bottom: 12px;
    font-size: 10.5px; color: #ffffff; letter-spacing: 0.4px;
  }

  /* Back */
  .back-brand {
    position: absolute; left: 0; right: 0; top: 34px;
    display: flex; align-items: center; justify-content: center; gap: 12px;
  }
  .back-brand__dot { width: 22px; height: 22px; border-radius: 50%; background: var(--olive); flex: none; }
  .back-brand__name { font-weight: 700; font-size: 28px; color: var(--olive); }
  .back-slogan {
    position: absolute; left: 0; right: 0; top: 84px;
    text-align: center; font-size: 12px; font-weight: 600; color: var(--green); letter-spacing: 0.3px;
  }
  .services {
    position: absolute; left: 0; right: 0; top: 114px;
    list-style: none; text-align: center;
  }
  .services__item { font-size: 11px; line-height: 17px; color: var(--ink); }
</style>
</head>
<body>
<main class="stage">

  <section class="card card--front" aria-label="Business card front">
    <svg class="card-bands" viewBox="0 0 520 298" aria-hidden="true">
      <path d="M0 212 C140 236 330 262 520 246 L520 252 C330 268 140 244 0 220 Z" fill="var(--gold)"/>
      <path d="M0 226 C140 252 330 272 520 262 L520 298 L0 298 Z" fill="var(--green)"/>
      <path d="M0 234 C140 260 330 280 520 270 L520 298 L0 298 Z" fill="var(--olive)"/>
    </svg>

    <div class="contact">
      <p class="contact__name">Darren Whitlow</p>
      <p class="contact__title">President</p>
      <ul class="contact__list">
        <li class="contact__item">
          <svg class="contact__icon" viewBox="0 0 10 10"><path d="M2 1 L4 3 L3 4.2 C3.8 5.6 4.4 6.2 5.8 7 L7 6 L9 8 L7.6 9.4 C4.5 8.8 1.2 5.5 0.6 2.4 Z" fill="var(--green)"/></svg>
          917.284.6051
        </li>
        <li class="contact__item">
          <svg class="contact__icon" viewBox="0 0 10 10"><rect x="1" y="1" width="8" height="8" fill="none" stroke="var(--green)" stroke-width="1.4"/></svg>
          917.512.7368
        </li>
        <li class="contact__item">
          <svg class="contact__icon" viewBox="0 0 10 10"><rect x="0.5" y="2" width="9" height="6.5" fill="var(--green)"/><path d="M0.5 2 L5 5.6 L9.5 2" fill="none" stroke="#fff" stroke-width="0.9"/></svg>
          Darren@silverbirchhelpers.com
        </li>
        <li class="contact__item">
          <svg class="contact__icon" viewBox="0 0 10 10"><circle cx="5" cy="5" r="4.3" fill="none" stroke="var(--green)" stroke-width="1.2"/><path d="M0.8 5 H9.2 M5 0.8 V9.2" stroke="var(--green)" stroke-width="0.9"/></svg>
          www.SilverBirchHelpers.com
        </li>
      </ul>
    </div>

    <div class="brand">
      <div class="brand__row">
        <span class="brand__dot"></span>
        <p class="brand__name">Silver Birch Helpers</p>
      </div>
      <p class="brand__slogan">Our Family. Caring For Yours.</p>
    </div>

    <p class="front-web">www.SilverBirchHelpers.com</p>
  </section>

  <section class="card card--back" aria-label="Business card back">
    <svg class="card-bands" viewBox="0 0 520 298" aria-hidden="true">
      <path d="M0 246 C190 262 380 236 520 212 L520 220 C380 244 190 268 0 252 Z" fill="var(--gold)"/>
      <path d="M0 262 C190 272 380 252 520 226 L520 298 L0 298 Z" fill="var(--green)"/>
      <path d="M0 270 C190 280 380 260 520 234 L520 298 L0 298 Z" fill="var(--olive)"/>
    </svg>

    <div class="back-brand">
      <span class="back-brand__dot"></span>
      <p class="back-brand__name">Silver Birch Helpers</p>
    </div>
    <p class="back-slogan">Our Family. Caring For Yours.</p>
    <ul class="services">
      <li class="services__item">Meal Preparation</li>
      <li class="services__item">Transportation</li>
      <li class="services__item">Light Housekeeping</li>
      <li class="services__item">Bathing Assistance</li>
      <li class="services__item">Companionship</li>
    </ul>
  </section>

</main>
</body>
</html>
```